Shopify Website for Health & Beauty

The user must be available to answer questions quickly if there's an issue. Good communication skills require.

*These products are unisex for men & women*
www.valtoro.com

Website we like to model
https://www.lumivelle-usa.com/
https://www.brindlow.com/
https://www.zenoxa.com/

Pages:
Home, about us, contact us, affiliate, search, blog

Need to redesign my current website valtoro.com
We need a high converting website
Custom banner
Social media setup
Graphics design
Lifestyle images
Create a new Site Icon/Favicon
Custom popups
Web content
Klayivo setup for flows and custom newsletters
Create a Custom 404 Page
Set SEO Titles and Meta Descriptions
Optimize Your Site's Performance
*Set Up Your Homepage
Add metadata to all pages
Use schema markup whenever possible
Check for technical SEO errors

```html
<!DOCTYPE html>
<html lang="en">
<head>
<meta charset="utf-8">
<title>Valtoro — Advanced Hair Care</title>
<link href="https://fonts.googleapis.com/css2?family=Nunito+Sans:wght@300;400;600;700&family=Montserrat:wght@300&display=swap" rel="stylesheet">
<style>
:root{
  --ink:#111111;
  --bar:#252525;
  --white:#ffffff;
  --red:#dd4f4f;
  --text:#222222;
  --muted:#555555;
  --line:#333333;
  --green-1:#2f5a2c;
  --green-2:#6f9a5e;
}
*{box-sizing:border-box;margin:0;padding:0}
html,body{width:1200px;height:3285px;overflow:hidden}
body{font-family:"Nunito Sans",sans-serif;color:var(--text);background:var(--white);position:relative}
a{color:inherit;text-decoration:none}
.announce{height:43px;background:var(--bar);color:var(--white);font-size:14px;display:flex;align-items:center;justify-content:center;letter-spacing:.2px}
.nav{height:82px;background:var(--ink);display:flex;align-items:center;padding:0 111px;color:var(--white)}
.brand{font-family:"Montserrat",sans-serif;font-weight:300;font-size:40px;letter-spacing:6px;color:var(--white)}
.menu{display:flex;gap:32px;margin-left:86px;font-size:16px;font-weight:600}
.nav-icons{display:flex;gap:36px;margin-left:auto;margin-right:0;padding-right:5px}
.hero{position:relative;height:650px}
.hero-photo{position:absolute;inset:0;background:radial-gradient(ellipse at 68% 45%,#5f8b52 0%,var(--green-1) 60%,#1f3d1c 100%)}
.hero-copy{position:absolute;left:111px;top:170px;color:var(--white);width:370px}
.hero-copy .brand{font-size:42px}
.hero-copy p{font-size:15px;line-height:25.5px;margin-top:16px}
.btn-light{display:inline-block;margin-top:16px;background:var(--white);color:var(--ink);font-weight:600;font-size:15px;padding:13px 26px}
.dots{position:absolute;left:111px;top:561px;display:flex;gap:7px}
.dots span{width:13px;height:13px;border-radius:50%;background:var(--white)}
.people{display:grid;grid-template-columns:repeat(5,1fr);height:128px;border-bottom:1px solid var(--line)}
.person{display:flex;align-items:center;gap:14px;padding-left:31px;border-right:1px solid var(--line)}
.person:last-child{border-right:0}
.avatar{width:76px;height:76px;border-radius:50%;background:linear-gradient(135deg,#6b3a26,#2a1a14)}
.person span{font-size:16px;line-height:21px}
.promos{position:absolute;top:1000px;left:111px;width:977px;display:flex;justify-content:space-between}
.promo{width:477px;height:452px;border:2px solid var(--ink);text-align:center}
.promo-photo{height:298px;background:linear-gradient(135deg,#8b6f60,#3b3036)}
.promo h3{font-weight:400;font-size:21px;margin-top:30px;letter-spacing:.5px}
.promo p{font-size:15px;margin-top:14px}
.btn-dark{display:inline-block;background:var(--ink);color:var(--white);font-size:14px;font-weight:600;padding:12px 23px;margin-top:20px}
.section-title{position:absolute;top:1543px;width:100%;text-align:center;font-size:40px;font-weight:600;letter-spacing:1px;color:var(--ink)}
.products{position:absolute;top:1626px;left:111px;width:977px;display:grid;grid-template-columns:repeat(3,312px);column-gap:20.5px;row-gap:0}
.product{height:523px;position:relative;text-align:center}
.bottle{width:92px;height:252px;margin:0 auto;border-radius:18px 18px 14px 14px;background:linear-gradient(90deg,#2c2c2c,#4a4a4a 50%,#2c2c2c)}
.heart{position:absolute;right:25px;top:6px}
.product h4{font-weight:400;font-size:20px;line-height:26px;height:52px;margin-top:30px;letter-spacing:.4px}
.size{font-size:19px;color:var(--muted);margin-top:2px}
.meta{display:flex;justify-content:space-between;align-items:center;padding:0 30px;margin-top:8px}
.stars{font-size:14px;letter-spacing:2px;color:var(--ink)}
.price{color:var(--red);font-size:20px}
.cart-btn{display:block;height:60px;line-height:60px;margin-top:14px;background:var(--ink);color:var(--white);font-size:20px;font-weight:600;letter-spacing:.5px}
.cart-btn.is-active{background:var(--red)}
.features{position:absolute;top:2710px;left:0;width:1200px;height:256px;display:grid;grid-template-columns:400px 400px 400px;border-top:1px solid var(--line)}
.feature{border-right:1px solid var(--line);padding:30px 0 0 58px}
.feature:nth-child(2){padding-left:57px}
.feature:nth-child(3){padding-left:57px}
.feature h5{font-weight:400;font-size:21px;margin-top:10px;letter-spacing:.5px;color:var(--ink)}
.feature p{font-size:13.5px;line-height:21.5px;color:var(--muted);margin-top:16px;width:300px}
.footer{position:absolute;top:2966px;left:0;width:1200px;height:319px;background:var(--ink);color:var(--white)}
.foot-links{position:absolute;left:111px;top:80px;font-size:14px;font-weight:600;line-height:34.3px}
.social{position:absolute;left:453px;top:80px;font-size:14px;font-weight:600;line-height:34.3px}
.social li{display:flex;align-items:center;gap:14px;list-style:none}
.social i{width:10px;height:10px;border-radius:50%;background:var(--red);display:inline-block}
.foot-links li{list-style:none}
.copyright{position:absolute;right:112px;top:81px;font-size:14px}
.payments{position:absolute;right:112px;top:118px;display:flex;gap:6px}
.payments span{width:42px;height:22px;background:var(--white);border-radius:3px}
</style>
</head>
<body>
<div class="announce">FREE SHIPPING ON ORDERS OVER $50</div>
<header class="nav">
  <div class="brand">VALTORO</div>
  <nav class="menu"><a>Home</a><a>About us</a><a>Contact us</a><a>Affiliate</a><a>Search</a><a>blog</a></nav>
  <div class="nav-icons">
    <svg width="12" height="14" viewBox="0 0 12 14" aria-label="Account"><circle cx="6" cy="4" r="3.2" fill="#fff"/><path d="M0 14c0-4 2.5-6 6-6s6 2 6 6z" fill="#fff"/></svg>
    <svg width="14" height="13" viewBox="0 0 14 13" aria-label="Cart"><path d="M0 1h2.5l2 7.5h7.5L14 3H4" fill="none" stroke="#fff" stroke-width="1.6"/><circle cx="5.5" cy="11.5" r="1.3" fill="#fff"/><circle cx="11" cy="11.5" r="1.3" fill="#fff"/></svg>
  </div>
</header>
<section class="hero">
  <div class="hero-photo" role="img" aria-label="Two dark shampoo bottles on wooden and green pedestals against a leafy green backdrop"></div>
  <div class="hero-copy">
    <div class="brand">VALTORO</div>
    <p>Lorem ipsum dolor sit amet, consectetur adipiscing elit, sed do eiusmod tempor incididunt ut labore et dolore magna aliqua.</p>
    <a class="btn-light">GET STARTED</a>
  </div>
  <div class="dots"><span></span><span></span><span></span></div>
</section>
<section class="people">
  <div class="person"><div class="avatar" role="img" aria-label="Portrait of a woman with curly red hair"></div><span>Lorem ipsum<br>dolor</span></div>
  <div class="person"><div class="avatar" role="img" aria-label="Portrait of a woman with wavy brown hair"></div><span>Lorem ipsum<br>dolor</span></div>
  <div class="person"><div class="avatar" role="img" aria-label="Portrait of a smiling man with glasses"></div><span>Lorem ipsum<br>dolor</span></div>
  <div class="person"><div class="avatar" role="img" aria-label="Portrait of a man with a beard"></div><span>Lorem ipsum<br>dolor</span></div>
  <div class="person"><div class="avatar" role="img" aria-label="Portrait of a bearded man on dark background"></div><span>Lorem ipsum<br>dolor</span></div>
</section>
<section class="promos">
  <article class="promo">
    <div class="promo-photo" role="img" aria-label="Stylist combing a smiling woman's wavy hair in a salon"></div>
    <h3>YOU DARE, WE CARE</h3>
    <p>New! Loyalty Rewards Program</p>
    <a class="btn-dark">LEARN MORE</a>
  </article>
  <article class="promo">
    <div class="promo-photo" role="img" aria-label="Hairdresser styling a bearded man's hair with a brush"></div>
    <h3>HAIR QUIZ</h3>
    <p>You're only 2 mins from your ideal routine.</p>
    <a class="btn-dark">LEARN MORE</a>
  </article>
</section>
<h2 class="section-title">BEST SELLERS</h2>
<section class="products">
  <article class="product"><div class="bottle" role="img" aria-label="Deluxe strengthening shampoo bottle"></div><svg class="heart" width="20" height="18" viewBox="0 0 20 18"><path d="M10 16.5S1.5 11 1.5 5.5A4 4 0 0 1 10 3.8 4 4 0 0 1 18.5 5.5C18.5 11 10 16.5 10 16.5z" fill="none" stroke="#111" stroke-width="1.4"/></svg><h4>DELUXE STRENGTHENING SHAMPOO</h4><div class="size">(8.5 OZ)</div><div class="meta"><span class="stars">★★★★★</span><span class="price">$24.70</span></div><a class="cart-btn">ADD TO CART</a></article>
  <article class="product"><div class="bottle" role="img" aria-label="Deluxe strengthening conditioner bottle"></div><svg class="heart" width="20" height="18" viewBox="0 0 20 18"><path d="M10 16.5S1.5 11 1.5 5.5A4 4 0 0 1 10 3.8 4 4 0 0 1 18.5 5.5C18.5 11 10 16.5 10 16.5z" fill="none" stroke="#111" stroke-width="1.4"/></svg><h4>DELUXE STRENGTHENING CONDITIONER</h4><div class="size">(8.5 OZ)</div><div class="meta"><span class="stars">★★★★★</span><span class="price">$26.39</span></div><a class="cart-btn is-active">ADD TO CART</a></article>
  <article class="product"><div class="bottle" role="img" aria-label="Deluxe renewal serum bottle"></div><svg class="heart" width="20" height="18" viewBox="0 0 20 18"><path d="M10 16.5S1.5 11 1.5 5.5A4 4 0 0 1 10 3.8 4 4 0 0 1 18.5 5.5C18.5 11 10 16.5 10 16.5z" fill="none" stroke="#111" stroke-width="1.4"/></svg><h4>DELUXE RENEWAL SERUM</h4><div class="size">(4 OZ)</div><div class="meta"><span class="stars">★★★★★</span><span class="price">$23.40</span></div><a class="cart-btn">ADD TO CART</a></article>
  <article class="product"><div class="bottle" role="img" aria-label="Deluxe deep treatment bottle"></div><svg class="heart" width="20" height="18" viewBox="0 0 20 18"><path d="M10 16.5S1.5 11 1.5 5.5A4 4 0 0 1 10 3.8 4 4 0 0 1 18.5 5.5C18.5 11 10 16.5 10 16.5z" fill="none" stroke="#111" stroke-width="1.4"/></svg><h4>DELUXE DEEP TREATMENT</h4><div class="size">(4 OZ)</div><div class="meta"><span class="stars">★★★★★</span><span class="price">$18.59</span></div><a class="cart-btn">ADD TO CART</a></article>
  <article class="product"><div class="bottle" role="img" aria-label="Deluxe renewal masque bottle"></div><svg class="heart" width="20" height="18" viewBox="0 0 20 18"><path d="M10 16.5S1.5 11 1.5 5.5A4 4 0 0 1 10 3.8 4 4 0 0 1 18.5 5.5C18.5 11 10 16.5 10 16.5z" fill="none" stroke="#111" stroke-width="1.4"/></svg><h4>DELUXE RENEWAL MASQUE</h4><div class="size">(4 OZ)</div><div class="meta"><span class="stars">★★★★★</span><span class="price">$21.84</span></div><a class="cart-btn">ADD TO CART</a></article>
  <article class="product"><div class="bottle" role="img" aria-label="Deluxe mint pomade container"></div><svg class="heart" width="20" height="18" viewBox="0 0 20 18"><path d="M10 16.5S1.5 11 1.5 5.5A4 4 0 0 1 10 3.8 4 4 0 0 1 18.5 5.5C18.5 11 10 16.5 10 16.5z" fill="none" stroke="#111" stroke-width="1.4"/></svg><h4>DELUXE MINT POMADE</h4><div class="size">(2 OZ)</div><div class="meta"><span class="stars">★★★★★</span><span class="price">$16.90</span></div><a class="cart-btn">ADD TO CART</a></article>
</section>
<section class="features">
  <div class="feature">
    <svg width="80" height="78" viewBox="0 0 80 78" fill="none" stroke="#dd4f4f" stroke-width="2"><path d="M42 14c-14 6-18 22-16 36 2 14 14 20 26 20s24-6 26-20c2-14-2-30-16-36"/><path d="M44 6l6 8 6-8"/><path d="M60 30c-3-3-10-2-10 3s10 4 10 9-7 6-10 3M55 26v4M55 46v4"/><rect x="2" y="52" width="18" height="22" rx="2"/><rect x="16" y="40" width="18" height="34" rx="2"/></svg>
    <h5>MONEY BACK GUARANTEE</h5>
    <p>Not satisfied with your order? Contact Us, We offer no hassle returns.</p>
  </div>
  <div class="feature">
    <svg width="80" height="78" viewBox="0 0 80 78" fill="none" stroke="#dd4f4f" stroke-width="2"><rect x="2" y="4" width="62" height="46" rx="3"/><path d="M2 14h62M2 22h62"/><rect x="12" y="38" width="60" height="36" rx="3"/><path d="M30 38v-8a12 12 0 0 1 24 0v8"/><circle cx="42" cy="54" r="4"/><path d="M18 66h26"/><circle cx="60" cy="66" r="3"/></svg>
    <h5>SECURE PAYMENT</h5>
    <p>Your safety is our priority. All payments are 100% secure.</p>
  </div>
  <div class="feature">
    <svg width="80" height="78" viewBox="0 0 80 78" fill="none" stroke="#dd4f4f" stroke-width="2"><path d="M58 20A30 30 0 1 0 36 68"/><path d="M56 8v12H44"/><path d="M22 34l8 8 14-16"/><path d="M42 52c0-6 12-6 12 0 0 5-12 10-12 18h13"/><path d="M70 70V48l-12 16h16"/></svg>
    <h5>SUPPORT 24/7</h5>
    <p>You will speak with one of our courteous representatives in 20 minutes or less.</p>
  </div>
</section>
<footer class="footer">
  <ul class="foot-links"><li>Return Policy</li><li>Search</li><li>Blog</li><li>Contact us</li><li>About us</li></ul>
  <ul class="social"><li><i></i>Circlebook</li><li><i></i>Chirper</li><li><i></i>Snapgram</li><li><i></i>Viewtube</li><li><i></i>Linkpro</li></ul>
  <div class="copyright">© Copyrights 2021 Company name | All Rights Reserved</div>
  <div class="payments" aria-label="Accepted payment methods"><span></span><span></span><span></span><span></span><span></span><span></span><span></span><span></span></div>
</footer>
</body>
</html>
```